logo & Business Card Design

BrightHaven Termite & Pest Control, I need a great logo, take my ideas and run with them!
I will use this in marketing and website so needs to be eye catching but professional

Target Market(s)

Resedintial & Business

Industry/Entity Type

Marketing

Contact Information for Business Card

Need front side with pertinent info & Logo; back side will have a 25% off initial services Coupon!

Font styles to use
Sans Serif

Colors
ec1f27
1b1b1b

Requirements
Must have
• Professional logo and style
Nice to have
• Raised lettering, black, red, white colors maybe? I'm flexible, but those colors go good on any background, vehicle, uniform, etc...
Should not have
• Cheesy

```html
<!DOCTYPE html>
<html lang="en">
<head>
<meta charset="utf-8">
<title>BrightHaven Termite &amp; Pest Control – Business Card</title>
<link href="https://fonts.googleapis.com/css2?family=Arimo:wght@400;700&family=Permanent+Marker&display=swap" rel="stylesheet">
<style>
  :root {
    --stage-top: #f4f4f4;
    --stage-bottom: #d9d9d9;
    --dark-top: #262626;
    --dark-bottom: #6a6a6a;
    --gold-top: #c4961c;
    --gold-bottom: #ecc02c;
    --brand-gold: #f2b51d;
    --ink: #2b2210;
    --rust: #a3300f;
    --white: #ffffff;
    --mark-top: #f3b81f;
    --mark-bottom: #7a4a08;
  }
  * { box-sizing: border-box; margin: 0; padding: 0; }
  html, body { width: 1200px; height: 450px; overflow: hidden; }
  body {
    background: linear-gradient(180deg, var(--stage-top), var(--stage-bottom));
    font-family: "Arimo", Arial, sans-serif;
    position: relative;
  }
  .card {
    position: absolute;
    top: 57px;
    width: 535px;
    height: 325px;
    box-shadow: 3px 5px 10px rgba(0,0,0,0.35);
    overflow: hidden;
  }
  .card-front { left: 60px; }
  .card-back {
    left: 621px;
    width: 534px;
    background: linear-gradient(180deg, var(--dark-top), var(--dark-bottom));
  }
  .front-brand-panel {
    position: absolute; left: 0; top: 0; width: 235px; height: 100%;
    background: linear-gradient(180deg, var(--dark-top), var(--dark-bottom));
  }
  .front-contact-panel {
    position: absolute; left: 235px; top: 0; right: 0; height: 100%;
    background: linear-gradient(180deg, var(--gold-top), var(--gold-bottom));
  }
  .brand-name {
    position: absolute; left: 0; width: 100%;
    text-align: center; color: var(--brand-gold); font-weight: 700;
    text-transform: uppercase; line-height: 1.25;
  }
  .brand-name .line-sub { display: block; }
  .front-brand-panel .brand-name { top: 44px; font-size: 19px; }
  .front-brand-panel .brand-name .line-sub { font-size: 11px; }
  .card-back .brand-name { top: 34px; font-size: 25px; }
  .card-back .brand-name .line-sub { font-size: 13px; }
  .brand-dot {
    position: absolute; border-radius: 50%;
    background: linear-gradient(180deg, var(--mark-top), var(--mark-bottom));
  }
  .front-brand-panel .brand-dot { width: 96px; height: 96px; left: 69px; top: 122px; }
  .card-back .brand-dot { width: 124px; height: 124px; left: 205px; top: 114px; }
  .tagline {
    position: absolute; left: 0; width: 100%; text-align: center;
    font-family: "Permanent Marker", sans-serif; font-style: italic;
    color: var(--white); text-transform: uppercase; letter-spacing: 0.5px;
  }
  .front-brand-panel .tagline { top: 246px; font-size: 12.5px; line-height: 1.3; }
  .card-back .tagline { top: 270px; font-size: 15.5px; }
  .person-name {
    position: absolute; left: 50px; top: 72px;
    font-size: 24px; font-weight: 400; color: var(--ink); text-transform: uppercase;
  }
  .person-title {
    position: absolute; left: 50px; top: 104px;
    font-size: 16px; color: var(--rust); text-transform: uppercase;
  }
  .faint-dot {
    position: absolute; left: 160px; top: 106px; width: 56px; height: 56px;
    border-radius: 50%; background: rgba(255,255,255,0.14);
  }
  .contact-row {
    position: absolute; left: 30px; display: flex; align-items: center; gap: 12px;
  }
  .contact-row svg { width: 17px; height: 17px; flex: none; }
  .contact-phone { top: 206px; font-size: 16px; color: var(--ink); }
  .contact-email { top: 231px; font-size: 11px; color: var(--ink); }
  .contact-web {
    position: absolute; left: 20px; top: 263px;
    font-size: 11px; color: var(--rust); text-transform: uppercase;
  }
</style>
</head>
<body>
  <section class="card card-front" aria-label="Business card front">
    <div class="front-brand-panel">
      <div class="brand-name">BrightHaven<span class="line-sub">Termite &amp; Pest Control</span></div>
      <div class="brand-dot" aria-hidden="true"></div>
      <p class="tagline">Safe, clean comfort<br>for your home or business</p>
    </div>
    <div class="front-contact-panel">
      <div class="faint-dot" aria-hidden="true"></div>
      <h1 class="person-name">Daniel Brooks</h1>
      <p class="person-title">President</p>
      <div class="contact-row contact-phone">
        <svg viewBox="0 0 20 20" aria-hidden="true">
          <circle cx="10" cy="10" r="9" fill="none" stroke="#a3300f" stroke-width="1.6"/>
          <path d="M6.5 5.5l2 0 1 2.5-1.3 1a6 6 0 0 0 2.8 2.8l1-1.3 2.5 1v2c0 .6-.5 1-1 1A8 8 0 0 1 5.5 6.5c0-.5.4-1 1-1z" fill="#a3300f"/>
        </svg>
        <span>251-555-0148</span>
      </div>
      <div class="contact-row contact-email">
        <svg viewBox="0 0 20 20" aria-hidden="true">
          <circle cx="10" cy="10" r="9" fill="none" stroke="#a3300f" stroke-width="1.6"/>
          <rect x="5" y="6.5" width="10" height="7" fill="#a3300f"/>
          <path d="M5 6.5l5 4 5-4" fill="none" stroke="#ecc02c" stroke-width="1"/>
        </svg>
        <span>DAN@BRIGHTHAVENPEST.COM</span>
      </div>
      <p class="contact-web">www.brighthavenpestcontrol.com</p>
    </div>
  </section>

  <section class="card card-back" aria-label="Business card back">
    <div class="brand-name">BrightHaven<span class="line-sub">Termite &amp; Pest Control</span></div>
    <div class="brand-dot" aria-hidden="true"></div>
    <p class="tagline">Safe, clean comfort for your home or business</p>
  </section>
</body>
</html>
```